Design for Employee Baseball Cards

Looking to design baseball cards for my employees. Trying to replicate famous baseball card design with swapping in an employee and listing there stats and fun facts. These cards will be inserted into boxes so customers can receive with their orders. Cards allow customers to put a face to the name they've always corresponded with, which makes their experience personable and more memorable.

Looking for a front and back design template. We are open to the design, but would like it to resemble a baseball/playing card.
Size: 2.5" x 3.5" vertical
Here is our website which can be referenced for color pallet and tone.
https://www.crateworksdirect.com/

Attached is an example of a vintage baseball. Can we see some versions like this?

Front
- Person's name
- Title/Department
- Crate Works Direct logo
- Person's photo - this will be an action shot like a baseball card

Back
I'm open to the design and content of the back. We want it to resemble a back of a baseball card as best as possible. Normally, baseball cards will have stats by year. Instead, we can have stats and fun facts like the following

Items for Back
- Bio
- Year started at CWD
- Department
- Years of experience
- Specialty
- Secret skill
- What you love about CWD
- Favorite quote
- Fun fact
- Passion outside of CWD
- Person's photo - we can include a smaller headshot

Font styles to use
Sans Serif

Colors
0054AA
0677BA
7BADD7
CADEEF
E8F1F8

Requirements
Must have
• The deliverable must be a template PSD or AI that we can swap in photos and edit text for each person's card.

```html
<!DOCTYPE html>
<html lang="en">
<head>
<meta charset="utf-8">
<title>Crate Works Direct – Employee Card Template</title>
<link href="https://fonts.googleapis.com/css2?family=Michroma&family=Roboto:ital,wght@0,400;0,500;1,400;1,500&display=swap" rel="stylesheet">
<style>
  :root {
    --navy: #1b3a6b;
    --royal: #0054aa;
    --sky: #0677ba;
    --line: #36a4e6;
    --pale: #cadeef;
    --ink: #111111;
    --paper: #ffffff;
    --stage: #6d6e72;
    --photo-a: #b9b7b2;
    --photo-b: #6f7f99;
  }
  * { margin: 0; padding: 0; box-sizing: border-box; }
  html, body { width: 877px; height: 1200px; overflow: hidden; background: var(--stage); }
  body { position: relative; font-family: "Roboto", Arial, sans-serif; }

  .card { position: absolute; top: 320px; width: 400px; height: 560px; overflow: hidden; }
  .card-front { left: 23px; background: var(--navy); }
  .card-back { left: 454px; background: var(--paper); }
  .card svg.shapes { position: absolute; inset: 0; }

  .brand { position: absolute; display: flex; align-items: center; gap: 8px; }
  .brand-mark { width: 24px; height: 24px; background: var(--navy); }
  .brand-name { font-size: 17px; font-weight: 500; line-height: 1.05; color: var(--navy); }
  .brand-tag { font-size: 5px; color: #555; margin-top: 2px; letter-spacing: .2px; }

  /* front */
  .front-brand { left: 26px; top: 22px; }
  .front-photo { position: absolute; left: 28px; top: 36px; width: 344px; height: 406px;
    border-radius: 0 22px 0 0; background: linear-gradient(160deg, var(--photo-a) 0%, #a3a6ab 55%, var(--photo-b) 100%); }
  .front-name { position: absolute; left: 38px; top: 463px; font-family: "Michroma", sans-serif;
    font-size: 20px; color: var(--paper); letter-spacing: 1px; }
  .front-title { position: absolute; left: 68px; top: 498px; font-size: 18px; font-style: italic; color: var(--paper); }

  /* back */
  .back-header { position: absolute; left: 17px; top: 17px; width: 223px; height: 139px; background: var(--navy);
    color: var(--paper); padding: 16px 0 0 17px; }
  .back-name { font-family: "Michroma", sans-serif; font-size: 21px; letter-spacing: 1px; margin-bottom: 8px; }
  .stat-row { display: flex; font-size: 13.5px; line-height: 18px; }
  .stat-row dt { width: 70px; }
  .back-photo { position: absolute; left: 240px; top: 17px; width: 143px; height: 139px;
    background: linear-gradient(170deg, #d6d6d3 0%, #b5b3ae 50%, var(--photo-b) 100%); }
  .fact-list { position: absolute; left: 62px; top: 186px; width: 300px; }
  .fact-list .stat-row { font-size: 12.5px; line-height: 17.8px; color: var(--ink); }
  .fact-list dt { width: 183px; }
  .note { position: absolute; left: 38px; width: 330px; font-size: 12.5px; line-height: 17.5px; color: var(--ink); text-align: justify; }
  .note h3 { font-size: 12.5px; font-weight: 500; font-style: italic; }
  .note-love { top: 340px; }
  .note-quote { top: 411px; }
  .back-brand { left: 33px; top: 486px; }
  .web-pill { position: absolute; left: 254px; top: 508px; width: 129px; height: 35px; border-radius: 10px 10px 0 0;
    background: var(--navy); color: var(--paper); font-size: 12px; display: flex; align-items: center; justify-content: center; }
</style>
</head>
<body>

<section class="card card-front" aria-label="Card front">
  <svg class="shapes" viewBox="0 0 400 560" width="400" height="560" aria-hidden="true">
    <defs>
      <linearGradient id="bannerFill" x1="0" y1="0" x2="0" y2="1">
        <stop offset="0" stop-color="#5b87cf"/>
        <stop offset=".5" stop-color="#2f5fae"/>
        <stop offset="1" stop-color="#3a6fc0"/>
      </linearGradient>
    </defs>
    <rect x="0" y="88" width="18" height="372" fill="var(--paper)"/>
    <line x1="20" y1="88" x2="20" y2="455" stroke="var(--line)" stroke-width="2"/>
    <rect x="372" y="150" width="14" height="270" fill="var(--paper)"/>
    <polygon points="400,405 400,560 235,560" fill="var(--ink)"/>
  </svg>
  <div class="front-photo" role="img" aria-label="Action photo of the employee"></div>
  <svg class="shapes" viewBox="0 0 400 560" width="400" height="560" aria-hidden="true">
    <polygon points="0,0 170,0 212,88 0,88" fill="var(--paper)"/>
    <polyline points="20,455 20,530 40,540 290,540 300,530" fill="none" stroke="var(--line)" stroke-width="2"/>
    <polygon points="0,455 262,455 282,495 0,495" fill="url(#bannerFill)"/>
    <rect x="20" y="495" width="227" height="30" rx="8" fill="var(--ink)"/>
  </svg>
  <div class="brand front-brand">
    <span class="brand-mark"></span>
    <div><div class="brand-name">Crate Works<br>Direct</div><div class="brand-tag">Boxes That Carry Your Brand</div></div>
  </div>
  <div class="front-name">JOHN DOE</div>
  <div class="front-title">Salesman</div>
</section>

<section class="card card-back" aria-label="Card back">
  <svg class="shapes" viewBox="0 0 400 560" width="400" height="560" aria-hidden="true">
    <path d="M0,375 Q10,372 17,370 L17,543 L0,560 Z" fill="var(--navy)"/>
    <path d="M0,378 L17,372 L17,560 L0,560 Z" fill="var(--navy)"/>
    <path d="M383,465 L400,460 L400,560 L383,560 Z" fill="var(--navy)"/>
    <rect x="0" y="543" width="400" height="17" fill="var(--navy)"/>
    <rect x="17" y="17" width="366" height="526" fill="none" stroke="var(--line)" stroke-width="2"/>
  </svg>
  <div class="back-header">
    <h2 class="back-name">JOHN DOE</h2>
    <dl>
      <div class="stat-row"><dt>HT</dt><dd>: 5’6”</dd></div>
      <div class="stat-row"><dt>WT</dt><dd>: 150</dd></div>
      <div class="stat-row"><dt>Born</dt><dd>: April 26, 1988</dd></div>
      <div class="stat-row"><dt>Home</dt><dd>: Lake Tahoe, CA</dd></div>
    </dl>
  </div>
  <div class="back-photo" role="img" aria-label="Headshot of the employee"></div>
  <dl class="fact-list">
    <div class="stat-row"><dt>Year Started at CWD</dt><dd>: 2000</dd></div>
    <div class="stat-row"><dt>Department</dt><dd>: IT</dd></div>
    <div class="stat-row"><dt>Years of Experience</dt><dd>: 22</dd></div>
    <div class="stat-row"><dt>Specialty</dt><dd>: Lorem ipsum</dd></div>
    <div class="stat-row"><dt>Secret Skill</dt><dd>: Lorem ipsum</dd></div>
    <div class="stat-row"><dt>Passion outside CWD</dt><dd>: Lorem ipsum</dd></div>
    <div class="stat-row"><dt>Fun Fact</dt><dd>: Lorem ipsum</dd></div>
  </dl>
  <div class="note note-love">
    <h3>What you love about CWD:</h3>
    <p>Lorem ipsum dolor sit amet, consectetuer adipiscing elit, sed diam nonummy nibh euismod tincidunt ut</p>
  </div>
  <div class="note note-quote">
    <h3>Favoutire quote:</h3>
    <p>Lorem ipsum dolor sit amet, consectetuer adipiscing elit, sed diam nonummy nibh euismod tincidunt ut</p>
  </div>
  <div class="brand back-brand">
    <span class="brand-mark"></span>
    <div><div class="brand-name">Crate Works<br>Direct</div><div class="brand-tag">Boxes That Carry Your Brand</div></div>
  </div>
  <div class="web-pill">crateworksdirect.com</div>
</section>

</body>
</html>
```